Quillon Banner Network Ads for Custom Software Company

We need some images for display on the Quillon Banner Network. Need a collection of them at different sizes.

This is for a custom software development company that specializes in small to medium size businesses.

PLEASE PLEASE PLEASE GET CREATIVE! That is the point! Something very typical and plain will not win!

Target Market(s)

Small and Medium sized businesses looking for custom software development services

Industry/Entity Type

Computer Software

Font styles to use
Serif
Sans Serif

Requirements
Must have
• Medium Rectangle (300×250)
• Large Rectangle (336×280)
• Leaderboard (728×90)
• Half Page (300×600)
• Large Mobile Banner (320×100)
• Needs to stand out, but not be obnoxious
• Needs to flow with the website design and colors (does not need to be the same colors, just needs to work together)
• Must have specific call to action (schedule appointment or read more are options, but feel free to make up more)
Nice to have
• Logo integration
• Adobe Illustrator files with artboards/exports for the different sizes
Should not have
• Should not have more than 20% text
• Don't steal from the slides on the website. We want "read more" to mean read more, not more of the same.

```html
<!DOCTYPE html>
<html lang="en">
<head>
<meta charset="utf-8">
<title>Corvessa – Quillon Banner Network Ad Set</title>
<link rel="stylesheet" href="https://fonts.googleapis.com/css2?family=Lato:wght@400;700;900&family=Montserrat:wght@500;600;700&display=swap">
<style>
  :root {
    --board: #c6c6c6;
    --navy: #05256a;
    --sky: #0894d4;
    --sky-soft: #2aa7e0;
    --white: #ffffff;
    --gold: #ffc000;
    --ink: #1b1b1b;
    --label: #333333;
  }
  * { box-sizing: border-box; margin: 0; padding: 0; }
  html, body { width: 1200px; height: 1200px; overflow: hidden; }
  body { background: var(--board); position: relative; font-family: "Montserrat", sans-serif; }

  .size-label {
    position: absolute;
    font-family: "Lato", sans-serif;
    font-size: 22px;
    color: var(--label);
    line-height: 1;
  }

  .banner { position: absolute; background: var(--navy); overflow: hidden; }
  .banner > * { position: absolute; z-index: 1; }
  .banner > .illustration { z-index: 0; }

  .illustration {
    border-radius: 40% 40% 12% 12%;
    background: linear-gradient(160deg, var(--sky-soft) 0%, var(--sky) 60%, rgba(8,148,212,0.55) 100%);
  }

  .brand { display: flex; align-items: center; color: var(--white); font-weight: 500; line-height: 1; white-space: nowrap; }
  .brand-mark { background: var(--white); flex: none; }

  .headline { color: var(--white); text-align: right; white-space: nowrap; line-height: 1; }
  .headline span { display: block; }

  .cta {
    display: flex; align-items: center; justify-content: center;
    background: var(--gold); color: var(--ink);
    font-family: "Lato", sans-serif; font-weight: 700; white-space: nowrap;
    box-shadow: 0 2px 3px rgba(0,0,0,0.25);
  }

  /* 300 x 250 */
  .medium-rect { left: 169px; top: 106px; width: 329px; height: 274px; }
  .medium-rect .illustration { left: 14px; top: 130px; width: 160px; height: 132px; }
  .medium-rect .brand { left: 160px; top: 29px; font-size: 22px; gap: 7px; }
  .medium-rect .brand-mark { width: 24px; height: 24px; }
  .medium-rect .headline { right: 18px; top: 82px; font-weight: 500; letter-spacing: 0.5px; }
  .medium-rect .headline .lead { font-size: 15px; margin-bottom: 8px; }
  .medium-rect .headline .main { font-size: 22px; }
  .medium-rect .cta { left: 184px; top: 136px; width: 81px; height: 28px; border-radius: 7px; font-size: 11px; }

  /* 336 x 280 */
  .large-rect { left: 160px; top: 456px; width: 369px; height: 307px; }
  .large-rect .illustration { left: 16px; top: 142px; width: 180px; height: 150px; }
  .large-rect .brand { left: 181px; top: 33px; font-size: 24px; gap: 8px; }
  .large-rect .brand-mark { width: 28px; height: 28px; }
  .large-rect .headline { right: 22px; top: 96px; font-weight: 600; letter-spacing: 0.5px; }
  .large-rect .headline .lead { font-size: 16px; margin-bottom: 9px; }
  .large-rect .headline .main { font-size: 24px; font-weight: 700; }
  .large-rect .cta { left: 207px; top: 153px; width: 91px; height: 31px; border-radius: 8px; font-size: 12px; }

  /* 300 x 600 */
  .half-page { left: 708px; top: 106px; width: 329px; height: 658px; }
  .half-page .illustration { left: 38px; top: 98px; width: 262px; height: 208px; }
  .half-page .brand { left: 52px; top: 396px; font-size: 40px; gap: 12px; }
  .half-page .brand-mark { width: 50px; height: 50px; }
  .half-page .headline { left: 33px; width: 270px; top: 482px; text-align: left; font-weight: 700; }
  .half-page .headline .lead { font-size: 23px; margin-bottom: 10px; letter-spacing: 0.8px; }
  .half-page .headline .main { font-size: 32px; letter-spacing: 0.5px; }
  .half-page .cta { left: 89px; top: 573px; width: 151px; height: 51px; border-radius: 12px; font-size: 21px; font-weight: 900; }

  /* 320 x 100 */
  .mobile-banner { left: 160px; top: 824px; width: 351px; height: 110px; }
  .mobile-banner .illustration { left: 8px; top: 22px; width: 72px; height: 62px; }
  .mobile-banner .brand { left: 265px; top: 37px; font-size: 12px; gap: 4px; }
  .mobile-banner .brand-mark { width: 12px; height: 12px; }
  .mobile-banner .headline { left: 90px; top: 37px; text-align: left; font-weight: 500; }
  .mobile-banner .headline .lead { font-size: 12px; margin-bottom: 7px; }
  .mobile-banner .headline .main { font-size: 18px; }
  .mobile-banner .cta { left: 272px; top: 58px; width: 53px; height: 17px; border-radius: 4px; font-size: 7px; }

  /* 728 x 90 */
  .leaderboard { left: 169px; top: 1006px; width: 799px; height: 98px; }
  .leaderboard .illustration { left: 42px; top: 14px; width: 88px; height: 72px; }
  .leaderboard .headline { left: 154px; top: 42px; text-align: left; font-size: 19px; font-weight: 500; letter-spacing: 1.3px; }
  .leaderboard .brand { left: 566px; top: 40px; font-size: 18px; gap: 5px; }
  .leaderboard .brand-mark { width: 20px; height: 20px; }
  .leaderboard .cta { left: 698px; top: 39px; width: 75px; height: 25px; border-radius: 6px; font-size: 10px; }
</style>
</head>
<body>

  <div class="size-label" style="left:169px; top:66px;">300_250</div>
  <div class="size-label" style="left:708px; top:66px;">300_600</div>
  <div class="size-label" style="left:169px; top:410px;">336_280</div>
  <div class="size-label" style="left:169px; top:786px;">320_100</div>
  <div class="size-label" style="left:175px; top:968px;">728_90</div>

  <section class="banner medium-rect">
    <div class="illustration" role="img" aria-label="Hand holding a serving tray with a lifted cloche revealing devices with gear icons"></div>
    <div class="brand"><span class="brand-mark"></span>Corvessa</div>
    <h2 class="headline"><span class="lead">A COMPLETE RANGE</span><span class="main">OF SOFTWARE</span></h2>
    <a class="cta">READ MORE</a>
  </section>

  <section class="banner large-rect">
    <div class="illustration" role="img" aria-label="Hand holding a serving tray with a lifted cloche revealing devices with gear icons"></div>
    <div class="brand"><span class="brand-mark"></span>Corvessa</div>
    <h2 class="headline"><span class="lead">A COMPLETE RANGE</span><span class="main">OF SOFTWARE</span></h2>
    <a class="cta">READ MORE</a>
  </section>

  <section class="banner half-page">
    <div class="illustration" role="img" aria-label="Hand holding a serving tray with a lifted cloche revealing devices with gear icons"></div>
    <div class="brand"><span class="brand-mark"></span>Corvessa</div>
    <h2 class="headline"><span class="lead">A COMPLETE RANGE</span><span class="main">OF SOFTWARE</span></h2>
    <a class="cta">READ MORE</a>
  </section>

  <section class="banner mobile-banner">
    <div class="illustration" role="img" aria-label="Hand holding a serving tray with a lifted cloche revealing devices with gear icons"></div>
    <h2 class="headline"><span class="lead">A COMPLETE RANGE</span><span class="main">OF SOFTWARE</span></h2>
    <div class="brand"><span class="brand-mark"></span>Corvessa</div>
    <a class="cta">READ MORE</a>
  </section>

  <section class="banner leaderboard">
    <div class="illustration" role="img" aria-label="Hand holding a serving tray with a lifted cloche revealing devices with gear icons"></div>
    <h2 class="headline">A COMPLETE RANGE OF SOFTWARE</h2>
    <div class="brand"><span class="brand-mark"></span>Corvessa</div>
    <a class="cta">READ MORE</a>
  </section>

</body>
</html>
```